Redesign Comparisson chart - make modern and effective

Use your imaginations to make a powerful distinction between QVR & other holistic modalities. There are 7 elements physical, mental, emotional, energetic, subconscious, superconscious and before and after testing.
We want it to be obvious that QVR is the only modality that works on all these elements simultaneously. We do not want to include any chakras as we want this information to be accepted by a wide range of people and belief systems.'

We want it to look simple but effective. Professional but powerful. We want QVR to stand out even of you eye just passed over i.
Updates

Hi everyone, thanks for your submissions so far. Basically what this image is meant to represent is a comparison chart between all the modalities There are 5 elements physical, mental, emotional, subconscious and superconscious. we want to reflect that QVR is the only modality that works on all these elements simultaneously. As we want the concept to be accepted and not considered woo woo, we want to steer away from chakras.

Target Market(s)

Professionals

Industry/Entity Type

Professional services

Font styles to use
Sans Serif
Other font styles liked:
• Poppins Monserratt

Colors
0094D4
00A9DD
6FCCEA
C7EBF8
E9F6FB

Requirements
Must have
• Clear/professional and clean look. Brand colours and logos. All typography and formats must be cohesive.
Nice to have
• More easy to read, different layout
Should not have
• Do not change the data just the way its presented. No chakras

```html
<!DOCTYPE html>
<html lang="en">
<head>
<meta charset="utf-8">
<title>QVR Modality Comparison Chart</title>
<link href="https://fonts.googleapis.com/css2?family=Poppins:wght@300;400;500;600;700&display=swap" rel="stylesheet">
<style>
  :root{
    --brand:#2cb3e4;
    --brand-deep:#1c8fc9;
    --ink:#1f1f1f;
    --panel:#eef4fb;
    --grid:#c9dbee;
    --physical:#dc4a40;
    --mental:#64bedc;
    --emotional:#62ad45;
    --energetic:#f39c35;
    --subconscious:#e8d04f;
    --superconscious:#7f6aa8;
    --testing:#d674aa;
  }
  *{margin:0;padding:0;box-sizing:border-box}
  html,body{width:1015px;height:1200px;overflow:hidden;background:#fff;font-family:"Poppins",sans-serif}
  .canvas{position:relative;width:1015px;height:1200px}
  .header{position:absolute;left:0;top:0;width:1015px;height:133px;background:#fff}
  .brand-dot{position:absolute;left:60px;top:66px;width:16px;height:16px;border-radius:50%;background:var(--brand)}
  .brand-name{position:absolute;left:84px;top:61px;color:var(--brand);font-weight:600;font-size:16px;line-height:26px;white-space:nowrap}
  .headline{position:absolute;left:230px;width:714px;top:46px;text-align:center;color:var(--brand);font-weight:600;font-size:16.5px;letter-spacing:.3px}
  .subline{position:absolute;left:220px;width:734px;top:72px;text-align:center;color:var(--ink);font-size:9.6px;line-height:12.6px}
  .panel{position:absolute;left:0;top:133px;width:1015px;height:1067px;background:var(--panel)}
  .desc{position:absolute;top:156px;width:92px;font-size:6.8px;line-height:8.2px;color:var(--ink);text-align:justify}
  .col-head{position:absolute;top:264px;width:101px;text-align:center;font-size:12.4px;font-weight:400;line-height:13px}
  .col-head.two{top:251px}
  .row-label{font-family:"Poppins",sans-serif;font-size:12.4px;font-weight:500;fill:var(--brand-deep);letter-spacing:.3px}
  .footer-name{position:absolute;left:640px;top:1146px;color:var(--brand);font-weight:700;font-size:22px}
  .footer-dot{position:absolute;left:624px;top:1156px;width:12px;height:12px;border-radius:50%;background:var(--brand)}
  .footer-rule{position:absolute;left:773px;top:1146px;width:1.5px;height:28px;background:var(--brand)}
  .footer-url{position:absolute;left:785px;top:1149px;color:var(--brand);font-weight:600;font-size:15.5px}
</style>
</head>
<body>
<div class="canvas">
  <header class="header">
    <div class="brand-dot"></div>
    <div class="brand-name">quiet vital renewal</div>
    <h1 class="headline">CHOOSE QVR FOR FAST, IMMEDIATE AND POWERFUL RESULTS</h1>
    <p class="subline">I MUST EXPERIENCE HEALING ON ALL LEVELS, I AM NOT JUST A BODY. I WANT TO LEARN HOW TO HEAL MYSELF, SO I'M NOT DEPENDENT ON OTHERS.<br>I WANT TO RELEASE ALL MY EMOTIONAL AND MENTAL BLOCKS, SO I CAN BE THE BEST VERSION OF MYSELF.</p>
  </header>

  <section class="panel"></section>

  <p class="desc" style="left:247px">Most modalities, including, a western medicine, focus on and treat the physical body only. The QVR process enables you to engage in healing your own body during the session. There is no muscle testing, no hands-on healing and no herbal remedies or medicines.</p>
  <p class="desc" style="left:349px">QVR enables you to use your own consciousness to self-heal. We don't give you advice or coaching, we allow your mind to heal itself.</p>
  <p class="desc" style="left:450px">QVR is the only modality that engages your emotions on a physical level. Emotions get stuck in your body and can cause illness over time if left unchecked. QVR enables you you experience fast and powerful emotional releasing</p>
  <p class="desc" style="left:551px">Most modalities try to move the energy in your body for you. QVR enables and empowers you to do it yourself.</p>
  <p class="desc" style="left:653px">Some modalities, like Kinesiology, access your subconscious through muscle testing. QVR empowers you to access your own subconscious and heal it yourself.</p>
  <p class="desc" style="left:754px">QVR is the only modality the enables you to access and heal your superconscious mind yourself.</p>
  <p class="desc" style="left:856px">QVR is the only modality the enables you to provide before and after results, which are documented by us, and analysed by you with our help.</p>

  <div class="col-head" style="left:243px;color:var(--physical)">PHYSICAL</div>
  <div class="col-head" style="left:345px;color:var(--mental)">MENTAL</div>
  <div class="col-head" style="left:446px;color:var(--emotional)">EMOTIONAL</div>
  <div class="col-head" style="left:547px;color:var(--energetic)">ENERGETIC</div>
  <div class="col-head" style="left:648px;color:var(--subconscious);font-size:11.2px">SUBCONSCIOUS</div>
  <div class="col-head" style="left:747px;width:105px;color:var(--superconscious);font-size:11.2px">SUPERCONSCIOUS</div>
  <div class="col-head two" style="left:851px;color:var(--testing);font-size:11.2px">BEFORE &amp;<br>AFTER TESTING</div>

  <svg width="1015" height="1200" style="position:absolute;left:0;top:0" xmlns="http://www.w3.org/2000/svg" aria-label="Comparison chart of QVR against other modalities">
    <g stroke-width="1.2">
      <line x1="273" y1="150" x2="313" y2="150" stroke="var(--physical)"/>
      <line x1="375" y1="150" x2="415" y2="150" stroke="var(--mental)"/>
      <line x1="476" y1="150" x2="516" y2="150" stroke="var(--emotional)"/>
      <line x1="577" y1="150" x2="617" y2="150" stroke="var(--energetic)"/>
      <line x1="678" y1="150" x2="718" y2="150" stroke="var(--subconscious)"/>
      <line x1="779" y1="150" x2="819" y2="150" stroke="var(--superconscious)"/>
      <line x1="881" y1="150" x2="921" y2="150" stroke="var(--testing)"/>
      <line x1="273" y1="262" x2="313" y2="262" stroke="var(--physical)"/>
      <line x1="375" y1="262" x2="415" y2="262" stroke="var(--mental)"/>
      <line x1="476" y1="262" x2="516" y2="262" stroke="var(--emotional)"/>
      <line x1="577" y1="262" x2="617" y2="262" stroke="var(--energetic)"/>
      <line x1="678" y1="262" x2="718" y2="262" stroke="var(--subconscious)"/>
      <line x1="779" y1="262" x2="819" y2="262" stroke="var(--superconscious)"/>
      <line x1="881" y1="249" x2="921" y2="249" stroke="var(--testing)"/>
    </g>

    <g stroke="var(--grid)" stroke-width="1">
      <line x1="242" y1="266" x2="242" y2="1129"/>
      <line x1="344" y1="266" x2="344" y2="1129"/>
      <line x1="445" y1="266" x2="445" y2="1129"/>
      <line x1="547" y1="266" x2="547" y2="1129"/>
      <line x1="648" y1="266" x2="648" y2="1129"/>
      <line x1="749" y1="266" x2="749" y2="1129"/>
      <line x1="851" y1="266" x2="851" y2="1129"/>
    </g>

    <g class="pins" stroke-width="1.2">
      <g stroke="var(--physical)" fill="var(--physical)"><circle cx="293" cy="282" r="2"/><line x1="293" y1="282" x2="293" y2="299"/></g>
      <g stroke="var(--mental)" fill="var(--mental)"><circle cx="395" cy="282" r="2"/><line x1="395" y1="282" x2="395" y2="299"/></g>
      <g stroke="var(--emotional)" fill="var(--emotional)"><circle cx="496" cy="282" r="2"/><line x1="496" y1="282" x2="496" y2="299"/></g>
      <g stroke="var(--energetic)" fill="var(--energetic)"><circle cx="597" cy="282" r="2"/><line x1="597" y1="282" x2="597" y2="299"/></g>
      <g stroke="var(--subconscious)" fill="var(--subconscious)"><circle cx="698" cy="282" r="2"/><line x1="698" y1="282" x2="698" y2="299"/></g>
      <g stroke="var(--superconscious)" fill="var(--superconscious)"><circle cx="799" cy="282" r="2"/><line x1="799" y1="282" x2="799" y2="299"/></g>
      <g stroke="var(--testing)" fill="var(--testing)"><circle cx="901" cy="282" r="2"/><line x1="901" y1="282" x2="901" y2="299"/></g>
    </g>

    <g class="qvr-row">
      <circle cx="62" cy="302" r="6" fill="var(--brand)"/>
      <text x="74" y="307" font-family="Poppins,sans-serif" font-weight="600" font-size="15" fill="var(--brand)">QVR</text>
      <rect x="251" y="299" width="83" height="14" fill="var(--physical)"/>
      <rect x="352.5" y="299" width="83" height="14" fill="var(--mental)"/>
      <rect x="454" y="299" width="83" height="14" fill="var(--emotional)"/>
      <rect x="555.5" y="299" width="83" height="14" fill="var(--energetic)"/>
      <rect x="657" y="299" width="83" height="14" fill="var(--subconscious)"/>
      <rect x="758.5" y="299" width="83" height="14" fill="var(--superconscious)"/>
      <rect x="860" y="299" width="83" height="14" fill="var(--testing)"/>
    </g>

    <g class="row-rules" stroke="var(--grid)" fill="var(--grid)">
      <line x1="171" y1="322" x2="957" y2="322"/><circle cx="171" cy="322" r="2" stroke="none"/>
      <line x1="171" y1="354.2" x2="957" y2="354.2"/><circle cx="171" cy="354.2" r="2" stroke="none"/>
      <line x1="171" y1="386.4" x2="957" y2="386.4"/><circle cx="171" cy="386.4" r="2" stroke="none"/>
      <line x1="171" y1="418.6" x2="957" y2="418.6"/><circle cx="171" cy="418.6" r="2" stroke="none"/>
      <line x1="171" y1="450.8" x2="957" y2="450.8"/><circle cx="171" cy="450.8" r="2" stroke="none"/>
      <line x1="171" y1="483" x2="957" y2="483"/><circle cx="171" cy="483" r="2" stroke="none"/>
      <line x1="171" y1="515.2" x2="957" y2="515.2"/><circle cx="171" cy="515.2" r="2" stroke="none"/>
      <line x1="171" y1="547.4" x2="957" y2="547.4"/><circle cx="171" cy="547.4" r="2" stroke="none"/>
      <line x1="171" y1="579.6" x2="957" y2="579.6"/><circle cx="171" cy="579.6" r="2" stroke="none"/>
      <line x1="171" y1="611.8" x2="957" y2="611.8"/><circle cx="171" cy="611.8" r="2" stroke="none"/>
      <line x1="171" y1="644" x2="957" y2="644"/><circle cx="171" cy="644" r="2" stroke="none"/>
      <line x1="171" y1="676.2" x2="957" y2="676.2"/><circle cx="171" cy="676.2" r="2" stroke="none"/>
      <line x1="171" y1="708.4" x2="957" y2="708.4"/><circle cx="171" cy="708.4" r="2" stroke="none"/>
      <line x1="171" y1="740.6" x2="957" y2="740.6"/><circle cx="171" cy="740.6" r="2" stroke="none"/>
      <line x1="171" y1="772.8" x2="957" y2="772.8"/><circle cx="171" cy="772.8" r="2" stroke="none"/>
      <line x1="171" y1="805" x2="957" y2="805"/><circle cx="171" cy="805" r="2" stroke="none"/>
      <line x1="171" y1="837.2" x2="957" y2="837.2"/><circle cx="171" cy="837.2" r="2" stroke="none"/>
      <line x1="171" y1="869.4" x2="957" y2="869.4"/><circle cx="171" cy="869.4" r="2" stroke="none"/>
      <line x1="171" y1="901.6" x2="957" y2="901.6"/><circle cx="171" cy="901.6" r="2" stroke="none"/>
      <line x1="171" y1="933.8" x2="957" y2="933.8"/><circle cx="171" cy="933.8" r="2" stroke="none"/>
      <line x1="171" y1="966" x2="957" y2="966"/><circle cx="171" cy="966" r="2" stroke="none"/>
      <line x1="171" y1="998.2" x2="957" y2="998.2"/><circle cx="171" cy="998.2" r="2" stroke="none"/>
      <line x1="171" y1="1030.4" x2="957" y2="1030.4"/><circle cx="171" cy="1030.4" r="2" stroke="none"/>
      <line x1="171" y1="1062.6" x2="957" y2="1062.6"/><circle cx="171" cy="1062.6" r="2" stroke="none"/>
      <line x1="171" y1="1094.8" x2="957" y2="1094.8"/><circle cx="171" cy="1094.8" r="2" stroke="none"/>
      <line x1="171" y1="1127" x2="957" y2="1127"/><circle cx="171" cy="1127" r="2" stroke="none"/>
    </g>

    <defs>
      <rect id="bar-p" x="251" y="9.2" width="83" height="14" fill="var(--physical)"/>
      <rect id="bar-m" x="352.5" y="9.2" width="83" height="14" fill="var(--mental)"/>
      <rect id="bar-en" x="555.5" y="9.2" width="83" height="14" fill="var(--energetic)"/>
      <rect id="bar-sub" x="657" y="9.2" width="83" height="14" fill="var(--subconscious)"/>
      <rect id="bar-sup" x="758.5" y="9.2" width="83" height="14" fill="var(--superconscious)"/>
      <rect id="bar-t" x="860" y="9.2" width="83" height="14" fill="var(--testing)"/>
    </defs>

    <g class="modality" transform="translate(0,322)"><text class="row-label" x="55" y="23">MASSAGE</text><use href="#bar-p"/></g>
    <g class="modality" transform="translate(0,354.2)"><text class="row-label" x="55" y="23">YOGA</text><use href="#bar-p"/></g>
    <g class="modality" transform="translate(0,386.4)"><text class="row-label" x="55" y="23">CHINESE MEDICINE</text><use href="#bar-p"/><use href="#bar-en"/><use href="#bar-t"/></g>
    <g class="modality" transform="translate(0,418.6)"><text class="row-label" x="55" y="23">CHIROPRACTIC</text><use href="#bar-p"/><use href="#bar-en"/><use href="#bar-sub"/><use href="#bar-t"/></g>
    <g class="modality" transform="translate(0,450.8)"><text class="row-label" x="55" y="23">KINESIOLOGY</text><use href="#bar-p"/><use href="#bar-sub"/><use href="#bar-t"/></g>
    <g class="modality" transform="translate(0,483)"><text class="row-label" x="55" y="23">NATROPATHY</text><use href="#bar-p"/></g>
    <g class="modality" transform="translate(0,515.2)"><text class="row-label" x="55" y="23">NUTRITIONAL HEALING</text><use href="#bar-p"/><use href="#bar-t"/></g>
    <g class="modality" transform="translate(0,547.4)"><text class="row-label" x="55" y="23">PSHYCHOLOGY</text><use href="#bar-m"/></g>
    <g class="modality" transform="translate(0,579.6)"><text class="row-label" x="55" y="23">MINDFULLNESS MEDITATION</text><use href="#bar-m"/><use href="#bar-t"/></g>
    <g class="modality" transform="translate(0,611.8)"><text class="row-label" x="55" y="23">LIFE COACHING</text><use href="#bar-m"/><use href="#bar-t"/></g>
    <g class="modality" transform="translate(0,644)"><text class="row-label" x="55" y="23">NLP</text><use href="#bar-m"/><use href="#bar-sub"/><use href="#bar-t"/></g>
    <g class="modality" transform="translate(0,676.2)"><text class="row-label" x="55" y="23">REIKI</text><use href="#bar-en"/></g>
    <g class="modality" transform="translate(0,708.4)"><text class="row-label" x="55" y="23">CRYSTAL HEALING</text><use href="#bar-en"/></g>
    <g class="modality" transform="translate(0,740.6)"><text class="row-label" x="55" y="23">BOWEN THERAPY</text><use href="#bar-p"/><use href="#bar-sub"/><use href="#bar-t"/></g>
    <g class="modality" transform="translate(0,772.8)"><text class="row-label" x="55" y="23">ENERGY MEDICINE</text><use href="#bar-en"/><use href="#bar-t"/></g>
    <g class="modality" transform="translate(0,805)"><text class="row-label" x="55" y="23">HYPNOTHERAPHY</text><use href="#bar-m"/><use href="#bar-sub"/></g>
    <g class="modality" transform="translate(0,837.2)"><text class="row-label" x="55" y="23">ACUPUNCTURE</text><use href="#bar-p"/><use href="#bar-en"/></g>
    <g class="modality" transform="translate(0,869.4)"><text class="row-label" x="55" y="23">TIMELINE THERAPY</text><use href="#bar-m"/><use href="#bar-sub"/><use href="#bar-t"/></g>
    <g class="modality" transform="translate(0,901.6)"><text class="row-label" x="55" y="23">INNER CHILD HEALING</text><use href="#bar-m"/><use href="#bar-sub"/></g>
    <g class="modality" transform="translate(0,933.8)"><text class="row-label" x="55" y="23">THETA HEALING</text><use href="#bar-sub"/><use href="#bar-sup"/></g>
    <g class="modality" transform="translate(0,966)"><text class="row-label" x="55" y="23">EFT</text><use href="#bar-p"/><use href="#bar-m"/><use href="#bar-sub"/><use href="#bar-t"/></g>
    <g class="modality" transform="translate(0,998.2)"><text class="row-label" x="55" y="23">FAMILY CONSTELLATION</text><use href="#bar-p"/><use href="#bar-m"/><use href="#bar-en"/></g>
    <g class="modality" transform="translate(0,1030.4)"><text class="row-label" x="55" y="23">PSYCHIC INTUITIVE</text><use href="#bar-p"/><use href="#bar-m"/></g>
    <g class="modality" transform="translate(0,1062.6)"><text class="row-label" x="55" y="23">AYURVEDIC MEDICINE</text><use href="#bar-p"/></g>
    <g class="modality" transform="translate(0,1094.8)"><text class="row-label" x="55" y="23">WESTERN MEDICINE</text><use href="#bar-p"/></g>
  </svg>

  <footer>
    <div class="footer-dot"></div>
    <div class="footer-name">brightwell</div>
    <div class="footer-rule"></div>
    <div class="footer-url">www.brightwell.com.au</div>
  </footer>
</div>
</body>
</html>
```